Proposal Template Design

We are looking to have our proposal templates redesigned. attached are examples of what we have been using. as well as our current logo

```html
<!DOCTYPE html>
<html lang="en">
<head>
<meta charset="UTF-8">
<title>Summit Seal Insulation Letterhead</title>
<link href="https://fonts.googleapis.com/css2?family=Poppins:wght@400;500;600;700&display=swap" rel="stylesheet">
<style>
  :root {
    --bg: #efefef;
    --paper: #ffffff;
    --ink: #1a1a1a;
    --brand-blue: #1c4c9c;
    --navy: #0b2a55;
    --sky: #1ba1dd;
    --mid-blue: #1b78bd;
  }
  * { box-sizing: border-box; margin: 0; padding: 0; }
  html, body { width: 783px; height: 1200px; overflow: hidden; }
  body { background: var(--bg); font-family: 'Poppins', sans-serif; color: var(--ink); }

  .letterhead {
    position: absolute; left: 21px; top: 77px;
    width: 740px; height: 1046px;
    background: var(--paper);
    box-shadow: 0 2px 10px rgba(0,0,0,.18);
    overflow: hidden;
  }

  .brand { position: absolute; left: 57px; top: 88px; display: flex; align-items: center; gap: 10px; }
  .brand-square { width: 22px; height: 22px; background: var(--navy); }
  .brand-name { font-weight: 700; font-size: 24px; line-height: 1.1; color: var(--navy); width: 210px; }

  .hero-art {
    position: absolute; left: 447px; top: 61px; width: 242px; height: 279px;
    background: linear-gradient(160deg, #f3f3f3, #e9e9e9);
    border-radius: 12px;
  }

  .sender { position: absolute; left: 57px; top: 232px; }
  .sender-name { font-weight: 700; font-size: 34px; line-height: 1.1; color: var(--brand-blue); }
  .sender-role { font-weight: 600; font-size: 19px; margin-top: 2px; }

  .letter { position: absolute; left: 57px; top: 334px; width: 628px; }
  .salutation { font-weight: 600; font-size: 15px; margin-bottom: 16px; }
  .letter p { font-size: 12.3px; line-height: 15px; text-align: justify; margin-bottom: 15px; }

  .signature { position: absolute; right: 55px; top: 806px; text-align: right; }
  .signature-name { font-weight: 700; font-size: 20px; line-height: 1.1; color: var(--brand-blue); }
  .signature-role { font-weight: 600; font-size: 17px; }

  .contacts { position: absolute; left: 57px; top: 940px; display: grid; grid-template-columns: 205px auto; row-gap: 8px; }
  .contact { display: flex; align-items: flex-start; gap: 8px; font-size: 12.5px; line-height: 15px; }
  .contact.large { font-size: 14px; }
  .contact svg { width: 18px; height: 18px; flex: none; }

  .footer-band { position: absolute; left: 0; bottom: 0; width: 740px; height: 80px; }
</style>
</head>
<body>
  <main class="letterhead">
    <div class="brand">
      <span class="brand-square"></span>
      <span class="brand-name">Summit Seal Insulation</span>
    </div>

    <div class="hero-art" role="img" aria-label="Faint line illustration of a spray foam gun"></div>

    <header class="sender">
      <h1 class="sender-name">LEO CARTER</h1>
      <p class="sender-role">Derector</p>
    </header>

    <section class="letter">
      <p class="salutation">Dear Sir,</p>
      <p>Thank you for the opportunity to present this proposal for your upcoming insulation project. Our team has reviewed the plans you shared and prepared a scope of work that covers every wall, attic and crawl space in the building. We use closed-cell and open-cell foam systems that seal gaps, block drafts and keep moisture out, helping the structure stay comfortable through every season while lowering monthly energy costs for many years to come after the work is complete.</p>
      <p>Before any work begins, a field technician will visit the site to measure each area, check the existing insulation and note any repairs that should be handled first. This visit lets us confirm material quantities, plan safe access for our crew and schedule the job around your other trades. Once the schedule is set, our installers arrive with all equipment, protect floors and fixtures, and apply foam to the agreed depth in each zone. Every pass is checked for thickness and coverage before the crew moves on, and all waste is removed from the site at the end of each working day. A final walk-through with your project lead closes out the job and confirms that every area meets the agreed standard.</p>
      <p>The pricing summary below is provided for those interested. Labour, materials and equipment are listed separately for each area of the building, along with the expected R-value, so the totals can be compared easily against any other quotes you may receive for this project.</p>
      <p>All of our installers are trained and certified in safe spray foam application, and every job is backed by a written warranty on both materials and workmanship. We carry full liability coverage and follow local building codes for fire ratings, ventilation and vapour control on every site we work on. If any issue appears after installation, our service team will return to inspect and correct it at no added cost to you. We look forward to working with you and are happy to answer any questions about this proposal at any time that suits you.</p>
    </section>

    <div class="signature">
      <p class="signature-name">MARK DALTON</p>
      <p class="signature-role">Manager</p>
    </div>

    <footer class="contacts">
      <div class="contact large">
        <svg viewBox="0 0 20 20" aria-hidden="true"><circle cx="10" cy="10" r="10" fill="#0b2a55"/><path d="M6.5 5.2l2 .1.8 2.3-1.2 1a6 6 0 0 0 3.3 3.3l1-1.2 2.3.8.1 2c-.4.6-1.2.9-2 .8A8 8 0 0 1 5.7 7.2c-.1-.8.2-1.6.8-2z" fill="#fff"/></svg>
        <span>555-210-4870</span>
      </div>
      <div class="contact">
        <svg viewBox="0 0 20 20" aria-hidden="true"><circle cx="10" cy="10" r="10" fill="#0b2a55"/><rect x="5" y="6.5" width="10" height="7" rx="1" fill="#fff"/><path d="M5.5 7l4.5 3.5L14.5 7" stroke="#0b2a55" stroke-width="1" fill="none"/></svg>
        <span>hello@summitsealfoam.com</span>
      </div>
      <div class="contact">
        <svg viewBox="0 0 20 20" aria-hidden="true"><path d="M10 1a6.5 6.5 0 0 0-6.5 6.5C3.5 12.5 10 19 10 19s6.5-6.5 6.5-11.5A6.5 6.5 0 0 0 10 1z" fill="#0b2a55"/><circle cx="10" cy="7.5" r="2.5" fill="#fff"/></svg>
        <span>820 Orchard Bend Rd<br>Fairview, TX 75000</span>
      </div>
      <div class="contact">
        <svg viewBox="0 0 20 20" aria-hidden="true"><circle cx="10" cy="10" r="10" fill="#0b2a55"/><g stroke="#fff" stroke-width="1" fill="none"><circle cx="10" cy="10" r="5.5"/><ellipse cx="10" cy="10" rx="2.3" ry="5.5"/><path d="M4.5 10h11M5.3 7.3h9.4M5.3 12.7h9.4"/></g></svg>
        <span>www.summitsealinsulation.com</span>
      </div>
    </footer>

    <svg class="footer-band" viewBox="0 0 740 80" aria-hidden="true">
      <defs>
        <linearGradient id="band-fade" x1="0" y1="0" x2="0" y2="1">
          <stop offset="0" stop-color="#1b78bd"/>
          <stop offset="1" stop-color="#0b2a55"/>
        </linearGradient>
      </defs>
      <polygon points="598,0 740,0 740,80 530,80 545,60" fill="url(#band-fade)"/>
      <polygon points="268,60 740,60 740,80 252,80" fill="#0b2a55"/>
      <polygon points="240,60 262,60 246,80 224,80" fill="#1ba1dd"/>
      <polygon points="580,0 594,0 538,60 524,60" fill="#1ba1dd"/>
    </svg>
  </main>
</body>
</html>
```